HOME IMPROVEMENT Business Card

I want a very unique business card. nothing typical and boring. Im open to you ideas. Ive seen cards with gold and silver or color foil and spot UV coatings. Im looking for something that looks cool and grabs attention. I like rounded corners but am open to all suggestions. We are a home improvement company and I will have a presentation folder printed and a catalog printed also and want to keep that same theme. I love the colors in our logo but I am open at looking at a 3rd color that would work with my logo. I hope that helps.
Card should include
Address
Phone
Fax
Email
Website
Target Market(s)
Home owners, people looking to remodel their home
Industry/Entity Type
Home Improvement
Contact Information for Business Card
2873 Maple Crest Avenue Unit 410
Ashford Vale, Il 60284
Phone
Direct Line
Email
Website
Font styles to use
Other font styles liked:
- IM OPEN MINDED
Requirements
Must have
- High end quality look nothing boring I like rounded corners but am open minded
Nice to have
- WOW. I want something nice and impressive.
Should not have
- ??? Not sure

```html
<!DOCTYPE html>
<html lang="en">
<head>
<meta charset="utf-8">
<title>Kestrel – Business Card</title>
<link rel="stylesheet" href="https://fonts.googleapis.com/css2?family=Open+Sans:wght@400;600;800&display=swap">
<style>
  :root {
    --bg: #c8c9ca;
    --card: #ffffff;
    --green: #079b48;
    --navy: #0c1446;
    --ink: #2b2b2b;
  }
  html, body {
    margin: 0;
    width: 1200px;
    height: 1200px;
    overflow: hidden;
    background: var(--bg);
  }
  .canvas {
    width: 1200px;
    height: 1200px;
    display: flex;
    flex-direction: column;
    align-items: center;
    justify-content: center;
    gap: 48px;
  }
  .card {
    width: 900px;
    height: 514px;
    display: block;
    background: var(--card);
    box-shadow: 0 6px 18px rgba(0,0,0,0.18);
  }
  .shape-green { fill: var(--green); }
  .shape-navy { fill: var(--navy); }
  .icon-disc { fill: var(--navy); }
  .icon-mark { fill: none; stroke: #fff; stroke-width: 2; stroke-linecap: round; stroke-linejoin: round; }
  .icon-solid { fill: #fff; }
  .contact-text {
    font-family: "Open Sans", sans-serif;
    font-size: 22px;
    font-weight: 400;
    fill: var(--ink);
  }
  .contact-text.strong { font-weight: 600; fill: #111; }
  .brand-name {
    font-family: "Open Sans", sans-serif;
    font-size: 96px;
    font-weight: 800;
    fill: var(--navy);
  }
</style>
</head>
<body>
<main class="canvas">

  <!-- Contact side -->
  <svg class="card card-back" viewBox="0 0 900 514" xmlns="http://www.w3.org/2000/svg" aria-label="Contact side of the business card">
    <rect width="900" height="514" fill="var(--card)"/>
    <polygon class="shape-green" points="0,0 527,0 0,272"/>
    <polygon class="shape-green" points="527,0 900,0 900,257"/>
    <rect class="shape-navy" x="0" y="442" width="900" height="36"/>

    <g class="contact-list">
      <g class="contact-row" transform="translate(250,215)">
        <circle class="icon-disc" r="15"/>
        <path class="icon-solid" d="M-6,-7 q-2,2 0,6 q4,7 10,9 q3,1 5,-1 l-3,-3 q-2,1 -4,-1 q-3,-2 -4,-5 q-1,-2 1,-3 z"/>
        <text class="contact-text strong" x="34" y="8">+18 5062 394418</text>
      </g>
      <g class="contact-row" transform="translate(250,260)">
        <circle class="icon-disc" r="15"/>
        <rect class="icon-mark" x="-8" y="-6" width="16" height="12"/>
        <path class="icon-mark" d="M-8,-6 L0,1 L8,-6"/>
        <text class="contact-text" x="34" y="8">INFO@KESTRELBUILD.COM</text>
      </g>
      <g class="contact-row" transform="translate(250,305)">
        <circle class="icon-disc" r="15"/>
        <circle class="icon-mark" r="8"/>
        <path class="icon-mark" d="M-8,0 H8 M0,-8 q-5,8 0,16 M0,-8 q5,8 0,16"/>
        <text class="contact-text" x="34" y="8">WWW.KESTRELBUILD.COM</text>
      </g>
      <g class="contact-row" transform="translate(250,350)">
        <circle class="icon-disc" r="15"/>
        <rect class="icon-mark" x="-8" y="-3" width="16" height="9"/>
        <rect class="icon-mark" x="-5" y="-9" width="10" height="6"/>
        <text class="contact-text" x="34" y="8">+18 6137 5920 3346</text>
      </g>
      <g class="contact-row" transform="translate(250,395)">
        <circle class="icon-disc" r="15"/>
        <path class="icon-solid" d="M0,9 L-6,0 A7,7 0 1 1 6,0 Z"/>
        <circle cx="0" cy="-3" r="2.5" fill="var(--navy)"/>
        <text class="contact-text" x="34" y="8">2873 Maple Crest Avenue Unit 410 Ashford Vale, Il 60284</text>
      </g>
    </g>
  </svg>

  <!-- Brand side -->
  <svg class="card card-front" viewBox="0 0 900 514" xmlns="http://www.w3.org/2000/svg" aria-label="Brand side of the business card">
    <rect width="900" height="514" fill="var(--card)"/>
    <polygon class="shape-green" points="0,0 527,0 0,272"/>
    <polygon class="shape-green" points="527,0 900,0 900,257"/>
    <rect class="shape-navy" x="0" y="442" width="900" height="36"/>

    <g class="brand-lockup">
      <rect class="shape-navy" x="318" y="262" width="28" height="28"/>
      <text class="brand-name" x="362" y="326">KESTREL</text>
    </g>
  </svg>

</main>
</body>
</html>
```